Marketing Business Card Design

I am, launching a marketing business where I will contract to market hospitality. I want something funky and fun to go with the name Pickle Pail

Industry/Entity Type

Marketing

Contact Information for Business Card

Marla Tennant-Greaves
Pickle Pail
Mobile: +61 2 407 392654
Email: marla@picklepail.com.au

Requirements
Must have
• Fun and modern
Should not have
• Not conservative

```html
<!DOCTYPE html>
<html lang="en">
<head>
<meta charset="utf-8">
<title>Pickle Pail – Business Card</title>
<link rel="stylesheet" href="https://fonts.googleapis.com/css2?family=EB+Garamond:ital,wght@0,400;0,700;1,400&family=Dancing+Script:wght@500&display=swap">
<style>
  :root {
    --red: #f9061b;
    --ink: #333333;
    --rule: #9a9a9a;
    --paper: #ffffff;
    --dot: #111111;
  }
  * { margin: 0; padding: 0; box-sizing: border-box; }
  html, body {
    width: 741px; height: 1200px; overflow: hidden;
    background: var(--paper);
  }
  .card {
    position: relative; width: 741px; height: 1200px;
    font-family: "EB Garamond", Georgia, serif; color: var(--ink);
  }
  .card-border {
    position: absolute; left: 45px; top: 43px; width: 651px; height: 1122px;
    border: 4px dotted var(--dot);
  }
  .brand {
    position: absolute; left: 0; top: 150px; width: 741px;
    display: flex; flex-direction: column; align-items: center; gap: 26px;
  }
  .brand-dot {
    width: 170px; height: 170px; border-radius: 50%; background: var(--red);
  }
  .brand-name {
    font-size: 64px; font-weight: 400; color: var(--red); letter-spacing: 1px;
  }
  .person {
    position: absolute; right: 88px; top: 620px; text-align: right;
  }
  .person-name { font-size: 38px; font-weight: 400; line-height: 1; padding-right: 52px; }
  .person-name strong { font-weight: 700; }
  .person-role { font-size: 28px; font-style: italic; margin-top: 8px; padding-right: 52px; }
  .person-bars { position: absolute; right: 0; top: 4px; }
  .divider {
    position: absolute; left: 90px; top: 719px; width: 561px; height: 1px; background: var(--rule);
  }
  .motto {
    position: absolute; left: 60px; top: 760px; width: 621px; text-align: center;
    font-family: "Dancing Script", cursive; font-size: 29px; line-height: 1.45; color: var(--red);
  }
  .contact {
    position: absolute; left: 0; top: 866px; width: 741px; text-align: center;
    font-size: 32px;
  }
  .contact-icon { display: block; margin: 0 auto; }
  .contact-phone { margin: 6px 0 10px; }
  .contact-email { margin-top: 4px; }
  .contact-abn { margin-top: 22px; }
  .contact-abn b { color: var(--red); font-weight: 700; font-size: 28px; }
</style>
</head>
<body>
<main class="card">
  <div class="card-border"></div>

  <header class="brand">
    <div class="brand-dot"></div>
    <div class="brand-name">Pickle Pail</div>
  </header>

  <section class="person">
    <h1 class="person-name"><strong>Marla</strong> Tennant-Greaves</h1>
    <p class="person-role">Director</p>
    <svg class="person-bars" width="38" height="34" viewBox="0 0 38 34" aria-hidden="true">
      <rect x="0" y="0" width="8" height="34" fill="var(--red)"/>
      <rect x="15" y="0" width="8" height="34" fill="var(--red)"/>
      <rect x="30" y="0" width="8" height="34" fill="var(--red)"/>
    </svg>
  </section>

  <div class="divider"></div>

  <p class="motto">“There’s no shortage of remarkable ideas, what’s<br>missing is the will to execute them.”</p>

  <section class="contact">
    <svg class="contact-icon" width="60" height="40" viewBox="0 0 60 40" aria-label="Phone">
      <path d="M4 12 C4 2 56 2 56 12 L56 16 L44 16 L44 10 L16 10 L16 16 L4 16 Z" fill="var(--red)"/>
      <path d="M16 16 L44 16 L54 38 L6 38 Z" fill="var(--red)"/>
      <circle cx="30" cy="27" r="6" fill="var(--paper)"/>
      <circle cx="30" cy="27" r="2.5" fill="var(--red)"/>
    </svg>
    <p class="contact-phone">+61 2 407 392654</p>
    <svg class="contact-icon" width="44" height="32" viewBox="0 0 44 32" aria-label="Email">
      <rect x="2" y="2" width="40" height="28" rx="2" fill="none" stroke="var(--red)" stroke-width="3"/>
      <path d="M3 4 L22 19 L41 4" fill="none" stroke="var(--red)" stroke-width="3"/>
    </svg>
    <p class="contact-email">marla@picklepail.com.au</p>
    <p class="contact-abn"><b>ABN</b> 31 572 808 419</p>
  </section>
</main>
</body>
</html>
```